The Timber Loft

We need a business card design for our wardrobe company.
Please visit our website www.zorvelcabinets.com to get an idea of who we are.

```html
<!DOCTYPE html>
<html lang="en">
<head>
<meta charset="utf-8">
<title>The Timber Loft — Business Card</title>
<link rel="stylesheet" href="https://fonts.googleapis.com/css2?family=Montserrat:wght@400;500;600&display=swap">
<style>
  :root {
    --backdrop: #2b2d30;
    --card-black: #0b0b0b;
    --card-black-edge: #1a1a1a;
    --card-gold: #a68c58;
    --gold-accent: #b0925a;
    --text-light: #d9d9d9;
    --text-white: #ffffff;
    --text-dark: #141414;
  }
  * { margin: 0; padding: 0; box-sizing: border-box; }
  html, body {
    width: 1200px;
    height: 900px;
    overflow: hidden;
  }
  body {
    background: var(--backdrop);
    font-family: "Montserrat", sans-serif;
    display: flex;
    align-items: center;
    justify-content: center;
    gap: 40px;
  }
  .card {
    width: 540px;
    height: 310px;
    border-radius: 26px;
    position: relative;
    overflow: hidden;
  }

  /* Front */
  .card-front {
    background: linear-gradient(160deg, var(--card-black-edge), var(--card-black) 55%);
    color: var(--text-light);
  }
  .brand {
    position: absolute;
    display: flex;
    align-items: flex-start;
    gap: 12px;
  }
  .brand-mark {
    width: 34px;
    height: 34px;
    border: 2px solid currentColor;
    flex: none;
  }
  .brand-name {
    font-size: 13px;
    font-weight: 600;
    letter-spacing: 0.04em;
    text-transform: uppercase;
    line-height: 1.2;
  }
  .brand-tagline {
    font-size: 12px;
    font-weight: 400;
    margin-top: 5px;
  }
  .card-front .brand {
    top: 40px;
    left: 40px;
    color: var(--text-white);
  }
  .contact {
    position: absolute;
    left: 240px;
    top: 96px;
  }
  .person-name {
    font-size: 28px;
    font-weight: 500;
    letter-spacing: 0.03em;
    line-height: 1.15;
    color: var(--text-white);
  }
  .person-title {
    font-size: 14px;
    color: var(--gold-accent);
    margin: 2px 0 14px;
  }
  .contact-list { list-style: none; }
  .contact-item {
    display: flex;
    align-items: flex-start;
    gap: 10px;
    font-size: 16px;
    line-height: 1.4;
    margin-bottom: 4px;
  }
  .contact-icon {
    width: 14px;
    height: 14px;
    flex: none;
    margin-top: 4px;
    fill: var(--gold-accent);
  }

  /* Back */
  .card-back {
    background: linear-gradient(150deg, #b19866, var(--card-gold) 50%, #9a804c);
    color: var(--text-dark);
    display: flex;
    align-items: center;
    justify-content: center;
  }
  .card-back .brand {
    position: static;
    gap: 16px;
  }
  .card-back .brand-mark { width: 48px; height: 48px; }
  .card-back .brand-name { font-size: 20px; }
  .card-back .brand-tagline { font-size: 16px; margin-top: 6px; }
</style>
</head>
<body>

  <section class="card card-front" aria-label="Business card front">
    <div class="brand">
      <span class="brand-mark" aria-hidden="true"></span>
      <div>
        <p class="brand-name">The Timber Loft</p>
        <p class="brand-tagline">Built Square and True</p>
      </div>
    </div>

    <div class="contact">
      <h1 class="person-name">YOUR NAME</h1>
      <p class="person-title">Job Title</p>
      <ul class="contact-list">
        <li class="contact-item">
          <svg class="contact-icon" viewBox="0 0 24 24" aria-hidden="true"><path d="M6.6 10.8a15.1 15.1 0 0 0 6.6 6.6l2.2-2.2a1 1 0 0 1 1-.25 11.4 11.4 0 0 0 3.6.57 1 1 0 0 1 1 1V20a1 1 0 0 1-1 1A17 17 0 0 1 3 4a1 1 0 0 1 1-1h3.5a1 1 0 0 1 1 1c0 1.25.2 2.45.57 3.57a1 1 0 0 1-.25 1z"/></svg>
          <span>0207 555 0148</span>
        </li>
        <li class="contact-item">
          <svg class="contact-icon" viewBox="0 0 24 24" aria-hidden="true"><path d="M2 5h20v14H2z"/><path d="M3.5 6.5 12 13l8.5-6.5" fill="none" stroke="#0b0b0b" stroke-width="1.6"/></svg>
          <span>info@zorvelcabinets.com</span>
        </li>
        <li class="contact-item">
          <svg class="contact-icon" viewBox="0 0 24 24" aria-hidden="true"><path d="M12 2a7 7 0 0 0-7 7c0 5.25 7 13 7 13s7-7.75 7-13a7 7 0 0 0-7-7zm0 9.5A2.5 2.5 0 1 1 12 6.5a2.5 2.5 0 0 1 0 5z"/></svg>
          <span>Harlow House, 42 Mill Lane<br>London E2 7QT</span>
        </li>
      </ul>
    </div>
  </section>

  <section class="card card-back" aria-label="Business card back">
    <div class="brand">
      <span class="brand-mark" aria-hidden="true"></span>
      <div>
        <p class="brand-name">The Timber Loft</p>
        <p class="brand-tagline">Built Square and True</p>
      </div>
    </div>
  </section>

</body>
</html>
```